Dentistry on Marlow Marketing Brochure

I require a brochure to market our practice and to send to new patients after they have made initial phone contact, in our 'new patient package' .
My preference is for a double sided A4 trifold brochure.
Please find attached the style guide and information to be included.
Also, please visit our website at www.dentistryonmarlow.com.au to get an idea of our brand- we prefer a clean, fresh look that still conveys warmth and professionalism.
The images from our website can be used for the brochure.
Please include the map attached.

```html
<!DOCTYPE html>
<html lang="en">
<head>
<meta charset="utf-8">
<title>Dentistry on Marlow – Brochure Inside</title>
<link rel="stylesheet" href="https://fonts.googleapis.com/css2?family=Didact+Gothic&family=Questrial&display=swap">
<style>
  :root {
    --accent: #dcdc1e;
    --accent-soft: #eeee8a;
    --heading-shadow: #4a4a2a;
    --text: #3a3a3a;
    --stripe-grey: #9a9a9a;
    --paper: #fbfbfb;
    --photo-warm: #d9cfc4;
    --photo-cool: #e7e7e2;
  }
  * { margin: 0; padding: 0; box-sizing: border-box; }
  html, body { width: 1200px; height: 846px; overflow: hidden; background: #fff; }
  .brochure {
    position: relative; width: 1200px; height: 846px;
    background: var(--paper);
    font-family: "Didact Gothic", "Questrial", sans-serif;
    color: var(--text);
    overflow: hidden;
  }
  .band-top {
    position: absolute; left: 0; top: 0; width: 100%; height: 32px;
    background: repeating-linear-gradient(to bottom, var(--accent) 0 2px, #fff 2px 5px);
  }
  .band-bottom {
    position: absolute; left: 0; bottom: 0; width: 100%; height: 32px;
    background: repeating-linear-gradient(to bottom, var(--stripe-grey) 0 2px, #fff 2px 5px);
  }
  .heading {
    position: absolute; text-align: center;
    font-family: "Questrial", sans-serif; font-weight: 700;
    font-size: 17px; color: var(--accent);
    text-shadow: 1px 1px 0 var(--heading-shadow);
    letter-spacing: -0.2px;
  }
  .heading .cap { font-size: 22px; }
  .copy {
    position: absolute; font-size: 14px; line-height: 17.2px;
    text-align: justify; letter-spacing: 0.3px;
  }
  .copy p { text-indent: 22px; margin-bottom: 17px; }
  .services {
    position: absolute; left: 78px; top: 492px; list-style: none;
    font-size: 14.5px; line-height: 23px; letter-spacing: 0.2px;
  }
  .services li { position: relative; padding-left: 21px; }
  .services li::before {
    content: ""; position: absolute; left: 0; top: 9px;
    width: 9px; height: 8px; border-radius: 2px; background: var(--accent);
  }
  .photo { position: absolute; }
  .photo-consult {
    left: 799px; top: 34px; width: 398px; height: 177px;
    background: linear-gradient(100deg, var(--photo-cool) 0%, #f1ece6 40%, var(--photo-warm) 70%, #c7c0c7 100%);
  }
  .photo-child {
    left: 406px; top: 374px; width: 393px; height: 192px;
    background: linear-gradient(90deg, #f2f2ee 0%, #e6ded5 45%, #d9c8b8 60%, #dfe9c8 100%);
  }
</style>
</head>
<body>
<main class="brochure">
  <div class="band-top"></div>
  <div class="band-bottom"></div>

  <!-- Left panel -->
  <h2 class="heading" style="left:34px; top:44px; width:340px;"><span class="cap">W</span>elcome</h2>
  <div class="copy" style="left:34px; top:87px; width:340px;">
    <p>At Dentistry on Marlow we offer an advanced standard of dental care services, using the most current philosophies and techniques. Our practitioners personalise dental care to your individual requirements, not only caring for your teeth and gums, but also caring about your general health and wellbeing.</p>
    <p>Our aim is to create and maintain sustainable healthy mouths for life, allowing you to feel comfortable and confident. This is achieved by our commitment to high quality, long lasting dental solutions when required and using preventive solutions for long term stability.</p>
    <p>We are so proud to be able to serve you with a comfortable, state-of-the-art facility and an award winning dental team who have been selected as the most caring, professional and highly respected in their field.</p>
  </div>
  <h2 class="heading" style="left:34px; top:455px; width:340px;"><span class="cap">O</span>ur <span class="cap">S</span>ervices <span class="cap">I</span>nclude:</h2>
  <ul class="services">
    <li>Dental implants</li>
    <li>CERAFORM ceramic restorations</li>
    <li>Restorations</li>
    <li>Root canal therapy</li>
    <li>Crown and bridge</li>
    <li>Veneers</li>
    <li>Hygiene care</li>
    <li>Whitening</li>
    <li>Children's dental care</li>
    <li>Mouthguards</li>
    <li>Gum treatment</li>
    <li>Sedation dentistry</li>
    <li>Digital radiographs and OPGs</li>
  </ul>

  <!-- Middle panel -->
  <h2 class="heading" style="left:425px; top:41px; width:349px;"><span class="cap">C</span>hild and <span class="cap">T</span>een <span class="cap">D</span>ental</h2>
  <div class="copy" style="left:430px; top:76px; width:344px;">
    <p>Dental decay rates are rapidly rising. To ensure our young patients have optimum dental health for life, Dentistry on Marlow is investing more time and effort into the care of our children and teenage patients.</p>
    <p>Our oral health therapists are our children's dental program practitioners, as they are specifically trained in children's dental care.</p>
    <p>Our OHTs have a special interest in the prevention of dental disease throughout the lifespan. They will provide you with the most current advice and product recommendations to suit your individual needs. They are specifically focused on giving your child the best head start they need to maintain a healthy smile for life.</p>
  </div>
  <div class="photo photo-child" role="img" aria-label="Photo of a smiling young girl with pigtails sitting in a dental chair"></div>
  <h2 class="heading" style="left:406px; top:575px; width:393px;"><span class="cap">C</span>hildren's <span class="cap">D</span>ental <span class="cap">D</span>ays</h2>
  <div class="copy" style="left:425px; top:613px; width:349px;">
    <p>Our children's days are fantastic for young children who haven't been to the dentist before or are shy or nervous about going to the dentist. This is a fun day where children can have their face painted, put on dress ups, get their teeth checked and go home with lots of rewards, a happy smile and a positive dental experience!</p>
    <p>Photos from our previous children's days are available on the Dentistry on Marlow Friendlink page.</p>
  </div>

  <!-- Right panel -->
  <div class="photo photo-consult" role="img" aria-label="Photo of a dentist showing a patient a dental model in a bright surgery"></div>
  <h2 class="heading" style="left:799px; top:225px; width:398px;"><span class="cap">H</span>ygiene <span class="cap">M</span>aintenance</h2>
  <div class="copy" style="left:834px; top:264px; width:325px;">
    <p>We have a strong focus on regular hygiene maintenance for all our patients and believe prevention of dental disease is smarter and more economical than treatment. There is a growing body of evidence highlighting the relationship between oral disease and systemic diseases such as cardiovascular disease, diabetes, arthritis and sleep apnoea.</p>
    <p>Emerging evidence suggests that improving oral health can actually lower your risk of some systemic diseases. We believe this increases the importance of maintaining optimum oral health, as it's not just for your teeth and gums, but for the benefit of your whole body.</p>
    <p>Your hygiene maintenance appointments are performed by a hygienist, practitioners who are qualified specifically in the prevention of dental disease. To save you time, these appointments are typically combined with your dental examination.</p>
    <p>Most people require a hygiene appointment every six months to maintain optimal oral health, however your hygienist will assess how often you should attend based on your needs. People with certain dental and health conditions may need to attend more frequently. As well as the benefits to your mouth and your body, your teeth will feel fantastic!</p>
  </div>
</main>
</body>
</html>
```